Boutique custom software development company needs new business card

Our nearly 20 year old custom software development company would like to better include the fact that we are now providing Bitcoin services. These new services are B2B include education (how to acquire and securely hold Bitcoin) and integrating Bitcoin payments into existing ecommerce sites or other existing systems. Please keep the card clean and simple. Attached is our current design and some other files. vexalon.example

Target Market(s)

businesses owners interested in long term relationship

Industry/Entity Type

Custom software development and Bitcoin

Contact Information for Business Card

Marcus Ellwood, marcus@vexalon.example, vexalon.example, (888) 555-VEXAL

Font styles to use
Other font styles liked:
• monospace

Requirements
Must have
• double-sided
Nice to have
• clean and simple
Should not have
• physical address

```html
<!DOCTYPE html>
<html lang="en">
<head>
<meta charset="utf-8">
<title>Vexalon Business Card</title>
<link rel="stylesheet" href="https://fonts.googleapis.com/css2?family=Courier+Prime:wght@400;700&family=Lato:wght@400;700&display=swap">
<style>
  :root {
    --orange: #f07823;
    --blue: #3e72c0;
    --white: #ffffff;
    --card-white: #fafafa;
    --ink-grey: #6f6f6f;
    --mono: "Courier Prime", "Courier New", monospace;
    --sans: "Lato", Arial, sans-serif;
  }
  * { margin: 0; padding: 0; box-sizing: border-box; }
  html, body { width: 1200px; height: 1200px; overflow: hidden; }
  body {
    position: relative;
    background: linear-gradient(to right, var(--white) 0 600px, var(--orange) 600px 1200px);
    font-family: var(--mono);
  }
  .card {
    position: absolute;
    width: 420px;
    height: 240px;
    box-shadow: 4px 6px 12px rgba(0,0,0,0.28);
  }
  .card-front {
    left: 348px; top: 393px;
    background: var(--orange);
    display: flex; flex-direction: column; align-items: center; justify-content: center;
    color: var(--white);
  }
  .front-name {
    font-family: var(--mono);
    font-weight: 700;
    font-size: 42px;
    letter-spacing: 1px;
    line-height: 1;
  }
  .front-tagline {
    margin-top: 8px;
    font-size: 9.5px;
    letter-spacing: 1.2px;
  }
  .card-back {
    left: 728px; top: 570px;
    background: var(--card-white);
  }
  .back-name {
    position: absolute; left: 25px; top: 22px;
    color: var(--blue);
    font-weight: 700;
    font-size: 14px;
    letter-spacing: 1.5px;
  }
  .back-rule {
    position: absolute; left: 25px; top: 46px;
    width: 135px; height: 1px; background: var(--orange);
  }
  .back-rule::after {
    content: ""; position: absolute; right: -2px; top: -1.5px;
    width: 4px; height: 4px; border-radius: 50%; background: var(--orange);
  }
  .back-details {
    position: absolute; left: 25px; top: 58px;
    color: var(--ink-grey);
    font-size: 10px;
    letter-spacing: 0.8px;
    line-height: 15px;
  }
  .back-details .gap { margin-top: 3px; }
  .back-mark {
    position: absolute; right: 22px; bottom: 22px;
    display: flex; flex-direction: column; align-items: center;
  }
  .mark-square {
    width: 70px; height: 70px; background: var(--blue);
  }
  .back-url {
    margin-top: 6px;
    color: var(--blue);
    font-size: 8px;
    letter-spacing: 0.6px;
  }
  .brand-block {
    position: absolute; left: 173px; top: 718px;
    width: 240px;
  }
  .brand-name {
    font-family: var(--mono);
    font-weight: 700;
    font-size: 46px;
    color: var(--blue);
    line-height: 1;
    letter-spacing: 0.5px;
  }
  .brand-tagline {
    margin-top: 6px;
    margin-left: 9px;
    font-family: var(--sans);
    font-size: 15px;
    color: var(--blue);
    letter-spacing: -0.4px;
  }
</style>
</head>
<body>
  <section class="card card-front" aria-label="Card front">
    <div class="front-name">VEXALON</div>
    <div class="front-tagline">custom software &amp; bitcoin services</div>
  </section>

  <section class="card card-back" aria-label="Card back">
    <div class="back-name">Marcus Ellwood</div>
    <div class="back-rule"></div>
    <div class="back-details">
      <div>(888) 555-VEXAL</div>
      <div>marcus@vexalon.example</div>
      <div class="gap">bitcoin education</div>
      <div>bitcoin payment integration</div>
    </div>
    <div class="back-mark">
      <div class="mark-square"></div>
      <div class="back-url">vexalon.example</div>
    </div>
  </section>

  <div class="brand-block">
    <div class="brand-name">VEXALON</div>
    <div class="brand-tagline">developer of custom applications</div>
  </div>
</body>
</html>
```